Marcus Penhale Logo and Wine Lable design

• What I am looking for is a packaging design to represent my product. The message I am looking for is a representation of western royal culture. Expensive and elegant. I want the label to look old, like from ancient times, feels like full of story, yet outstanding on the shelf among others. Special printing technique or paper can be used for an aged appearance.
• The packaging should include the logo, bottle, and the box that contains 12 bottle of wine.
• Shiraz
• Brand name Marcus Penhale must be included.
• Logo design should follow the same concept as above.
• There must be two labels, one on the front and one on the back of the bottle. The front label will carry most of the graphical impact.
• The back label should include some text for the wine, this could be anything, it is up to the design to present the story or testing of the wine in the test, which should also follow the concept above.
• The back label must have a standard space for barcode
• The label of packaging solution should also compline with the Cask Origin Scheme of Vintner Board.
• Final artwork ready for the printer should be provided in PDF format on CD, and include all fonts, images etc needed for printing
Updates

Project Deadline Extended
Reason: Hi guys, I am extending the deadline of this project as i am still seeking the design that could fulfill all my requirements, most important of all, as wine label, designs need to compliance with the Australia wine label requirement. in the extension, I will provide feed back to my designers proactively to find the right design that fits my requirement. Tam

Project Deadline Extended
Reason: waiting on the finalization on same designs

Industry/Entity Type

Printer

```html
<!DOCTYPE html>
<html lang="en">
<head>
<meta charset="utf-8">
<title>Marcus Penhale – Identity and Shipper Carton</title>
<link rel="stylesheet" href="https://fonts.googleapis.com/css2?family=Italianno&family=Lato:wght@400&display=swap">
<style>
  :root {
    --parchment: #d5c9a0;
    --sheet: #efefef;
    --ink: #6b2f16;
    --kraft: #b59049;
    --kraft-edge: #8f6e33;
    --crease: #e4e0d6;
    --base-band: #4a4030;
    --photo-light: #c9a88a;
    --photo-dark: #5e2a14;
    --fine-print: #4b3a22;
  }
  * { margin: 0; padding: 0; box-sizing: border-box; }
  html, body { width: 1200px; height: 1200px; overflow: hidden; }
  body { position: relative; background: var(--sheet); font-family: "Lato", sans-serif; }

  .brand-panel {
    position: absolute; left: 0; top: 0; width: 1200px; height: 696px;
    background: var(--parchment);
  }
  .estate-photo {
    position: absolute; left: 468px; top: 221px; width: 269px; height: 187px;
    background: radial-gradient(ellipse at 50% 60%, var(--photo-light) 0%, #a06d4e 55%, var(--photo-dark) 100%);
  }
  .wordmark {
    position: absolute; left: 0; top: 420px; width: 1200px; text-align: center;
    font-family: "Italianno", cursive; font-size: 190px; line-height: 1;
    color: var(--ink); letter-spacing: 2px;
  }

  .carton-dieline { position: absolute; left: 0; top: 696px; width: 1200px; height: 504px; }
  .carton-dieline svg { position: absolute; left: 0; top: 0; }

  .side-brand {
    position: absolute; width: 290px; text-align: center;
  }
  .side-brand .mini-photo {
    display: block; margin: 0 auto; width: 60px; height: 41px;
    background: radial-gradient(ellipse at 50% 60%, var(--photo-light), var(--photo-dark));
  }
  .side-brand .mini-wordmark {
    display: block; margin-top: 8px;
    font-family: "Italianno", cursive; font-size: 52px; line-height: 1; color: var(--fine-print);
  }
  .side-info {
    position: absolute; display: flex; align-items: center; gap: 10px;
  }
  .side-info .maker-lines {
    font-size: 6px; line-height: 9px; color: var(--fine-print); width: 150px;
  }
  .handling-marks { display: flex; gap: 4px; }
  .handling-marks span {
    width: 16px; height: 16px; border: 1.5px solid var(--fine-print);
  }
</style>
</head>
<body>

<section class="brand-panel">
  <div class="estate-photo" role="img" aria-label="Sepia photograph of a columned stately manor house framed by trees"></div>
  <h1 class="wordmark">Marcus Penhale</h1>
</section>

<section class="carton-dieline">
  <svg width="1200" height="504" viewBox="0 696 1200 504" aria-hidden="true">
    <g fill="var(--kraft)" stroke="var(--crease)" stroke-width="3">
      <!-- top flaps -->
      <rect x="53" y="749" width="295" height="127"/>
      <rect x="353" y="749" width="252" height="127"/>
      <rect x="610" y="749" width="290" height="127"/>
      <rect x="905" y="749" width="257" height="127"/>
      <!-- side walls -->
      <rect x="53" y="876" width="295" height="132"/>
      <rect x="353" y="876" width="252" height="132"/>
      <rect x="610" y="876" width="290" height="132"/>
      <rect x="905" y="876" width="257" height="132"/>
      <!-- bottom flaps -->
      <rect x="53" y="1014" width="295" height="131"/>
      <rect x="353" y="1014" width="252" height="131"/>
      <rect x="610" y="1014" width="290" height="131"/>
      <rect x="905" y="1014" width="257" height="131"/>
      <!-- glue tab -->
      <polygon points="24,888 53,876 53,1008 24,996"/>
    </g>
    <rect x="24" y="1006" width="1138" height="8" fill="var(--base-band)"/>
  </svg>

  <div class="side-brand" style="left:58px; top:204px;">
    <span class="mini-photo" role="img" aria-label="Small sepia photograph of the manor house"></span>
    <span class="mini-wordmark">Marcus Penhale</span>
  </div>
  <div class="side-brand" style="left:610px; top:204px;">
    <span class="mini-photo" role="img" aria-label="Small sepia photograph of the manor house"></span>
    <span class="mini-wordmark">Marcus Penhale</span>
  </div>

  <div class="side-info" style="left:365px; top:265px;">
    <div class="maker-lines">Penhale Estate Wines Pty Ltd<br>Barossa Road, South Australia</div>
    <div class="handling-marks"><span></span><span></span><span></span></div>
  </div>
  <div class="side-info" style="left:920px; top:265px;">
    <div class="maker-lines">Penhale Estate Wines Pty Ltd<br>Barossa Road, South Australia</div>
    <div class="handling-marks"><span></span><span></span><span></span></div>
  </div>
</section>

</body>
</html>
```